Photo Scanning New Business, Needs flyer design to capture Christmas gift ideas

Need a A5 size flyer for our business. Were a new business offering photo scanning and just about to go online. customers send us their old photos, slides or negatives from under their beds or in their cupboards and we then scan and digitize them and place onto a dvd or usb stick so they can view on their tv or computer anytime anywhere. Scanning old pictures isnt new bt very time consuming. Many customers like to download their photos from their digital cameras onto different social media websites, but their old photos they cant. Old photos also degrade and can get damaged.

I have included a design i was messing around with, which gives you the concept and wording im trying to get across in this flyer.

Target Market(s)

35 years and older. family members

Industry/Entity Type

Computer

Requirements
Must have
• the add must show the offer of "500 photos scanned for $50.00 Only"
Also have some words around " Make a great Christmas gift"

Needs to describe what the business is about
Nice to have
• please see my a5 flyer deisgn. colourful pictures. the flyer will be aimed at the christmas market, and hoping that people look at this and think that $50 is not alot of money for a christmas gift for one of the family, and that having all their pictures scanned is actually a good idea. Keeps them safe from Fire, Flood and Damage.
Should not have
• should not use cartoon style design

```html
<!DOCTYPE html>
<html lang="en">
<head>
<meta charset="utf-8">
<title>PictoVault – Christmas Flyer</title>
<link rel="stylesheet" href="https://fonts.googleapis.com/css2?family=Jost:ital,wght@0,300;0,400;0,500;1,400&display=swap">
<style>
  :root {
    --stage: #e9e9eb;
    --card: #8794ab;
    --card-warm: #a79aae;
    --ink: #f4f1ea;
    --cream: #ece3d3;
    --rule: rgba(244, 241, 234, 0.85);
  }
  html, body {
    margin: 0;
    width: 1200px;
    height: 800px;
    overflow: hidden;
    background: var(--stage);
    font-family: "Jost", "Futura", sans-serif;
  }
  .stage {
    position: relative;
    width: 1200px;
    height: 800px;
  }
  .flyer {
    position: absolute;
    display: block;
  }
  .flyer--front { left: 165px; top: 112px; width: 412px; height: 573px; }
  .flyer--back  { left: 613px; top: 110px; width: 407px; height: 575px; }
  .flyer text { fill: var(--ink); font-family: "Jost", "Futura", sans-serif; }
  .headline { font-size: 14.5px; letter-spacing: 0.6px; font-weight: 400; }
  .subhead { font-size: 8.5px; letter-spacing: 0.4px; }
  .step-label { font-size: 5.5px; }
  .benefit { font-size: 9.5px; letter-spacing: 0.2px; }
  .web { font-size: 5px; }
  .offer { font-size: 15px; font-style: italic; letter-spacing: 0.8px; }
  .brand-name { font-size: 15px; font-weight: 500; }
  .icon { fill: var(--ink); }
  .icon-line { stroke: var(--ink); fill: none; }
  .connector { stroke: var(--ink); stroke-width: 0.9; fill: none; }
  .connector--dashed { stroke-dasharray: 3 2.5; }
  .rule { stroke: var(--rule); stroke-width: 0.8; }
</style>
</head>
<body>
<main class="stage">

  <!-- Front of flyer -->
  <svg class="flyer flyer--front" viewBox="0 0 412 573" aria-label="Flyer front">
    <defs>
      <radialGradient id="front-wash" cx="0.55" cy="0.45" r="0.7">
        <stop offset="0" stop-color="var(--card-warm)"/>
        <stop offset="1" stop-color="var(--card)"/>
      </radialGradient>
    </defs>
    <rect width="412" height="573" fill="url(#front-wash)"/>
    <rect class="tree-illustration" x="63" y="133" width="282" height="307" rx="6"
          fill="var(--cream)" opacity="0.9" role="img"
          aria-label="Christmas tree illustration with star on top and bead garlands"/>
    <g class="brand">
      <rect x="158" y="538" width="14" height="14" fill="var(--ink)"/>
      <text class="brand-name" x="178" y="551">PictoVault</text>
    </g>
  </svg>

  <!-- Back of flyer -->
  <svg class="flyer flyer--back" viewBox="0 0 407 575" aria-label="Flyer back">
    <defs>
      <radialGradient id="back-wash" cx="0.2" cy="0.45" r="0.75">
        <stop offset="0" stop-color="var(--card-warm)"/>
        <stop offset="1" stop-color="var(--card)"/>
      </radialGradient>
    </defs>
    <rect width="407" height="575" fill="url(#back-wash)"/>
    <rect class="frame" x="12.5" y="12.5" width="382" height="550" fill="none" stroke="var(--rule)" stroke-width="0.9"/>

    <text class="headline" x="203" y="38" text-anchor="middle">BRING BACK TO LIFE YOUR OLD PHOTOS</text>
    <line class="rule" x1="55" y1="43" x2="352" y2="43"/>
    <text class="subhead" x="203" y="55" text-anchor="middle">Photo, Slide and Negative Scanning</text>

    <!-- Process diagram -->
    <g class="process">
      <!-- camera -->
      <g class="step step--capture">
        <rect class="icon" x="64" y="237" width="26" height="17" rx="2"/>
        <rect class="icon" x="70" y="233" width="9" height="5" rx="1"/>
        <circle cx="77" cy="245.5" r="5" fill="var(--card)"/>
        <circle class="icon" cx="77" cy="245.5" r="3"/>
        <text class="step-label" x="77" y="264" text-anchor="middle">Take your old photo</text>
      </g>
      <line class="connector" x1="97" y1="245" x2="138" y2="245"/>
      <path class="icon" d="M138 242 L142 245 L138 248 Z"/>

      <!-- scanner -->
      <g class="step step--scan">
        <rect class="icon" x="153" y="234" width="12" height="5"/>
        <rect class="icon" x="147" y="240" width="24" height="10" rx="1.5"/>
        <rect class="icon" x="152" y="251" width="14" height="4"/>
        <text class="step-label" x="159" y="264" text-anchor="middle">Scan It</text>
      </g>
      <line class="connector" x1="178" y1="245" x2="222" y2="245"/>
      <path class="icon" d="M222 242 L226 245 L222 248 Z"/>

      <!-- gear -->
      <g class="step step--process">
        <circle class="icon-line" cx="245" cy="244" r="6.5" stroke-width="4" stroke-dasharray="2.6 1.5"/>
        <circle class="icon" cx="245" cy="244" r="5.5"/>
        <circle cx="245" cy="244" r="2.3" fill="var(--card)"/>
        <text class="step-label" x="245" y="264" text-anchor="middle">Process It</text>
      </g>

      <!-- socialize -->
      <line class="connector connector--dashed" x1="245" y1="188" x2="245" y2="234"/>
      <g class="step step--socialize">
        <text class="step-label" x="245" y="102" text-anchor="middle">Socialize It</text>
        <circle class="icon" cx="245" cy="120" r="10"/>
        <circle class="icon" cx="245" cy="148" r="10"/>
        <circle class="icon" cx="245" cy="177" r="10"/>
      </g>

      <!-- share -->
      <line class="connector connector--dashed" x1="255" y1="234" x2="294" y2="200"/>
      <g class="step step--share">
        <text class="step-label" x="313" y="172" text-anchor="middle">Share It</text>
        <circle class="icon" cx="318" cy="181" r="4"/>
        <path class="icon" d="M311 196 Q311 187 318 187 Q325 187 325 196 Z"/>
        <circle class="icon" cx="311" cy="183" r="4"/>
        <path class="icon" d="M303 198 Q303 189 311 189 Q319 189 319 198 Z"/>
      </g>

      <!-- archive -->
      <line class="connector connector--dashed" x1="256" y1="244" x2="305" y2="244"/>
      <g class="step step--archive">
        <rect class="icon" x="313" y="235" width="24" height="5"/>
        <rect class="icon" x="315" y="241" width="20" height="12"/>
        <rect x="321" y="244" width="8" height="2" fill="var(--card)"/>
        <text class="step-label" x="329" y="262" text-anchor="middle">Archive It</text>
        <path class="icon" d="M344 244 h3 v7 h16 v-7 h3 v10 h-22 Z"/>
        <path class="icon" d="M355 233 L361 240 h-4 v7 h-4 v-7 h-4 Z"/>
      </g>

      <!-- send -->
      <line class="connector connector--dashed" x1="255" y1="254" x2="294" y2="285"/>
      <g class="step step--send">
        <rect class="icon" x="303" y="286" width="24" height="16" rx="1"/>
        <path d="M303 287 L315 296 L327 287" stroke="var(--card)" stroke-width="1.4" fill="none"/>
        <text class="step-label" x="315" y="310" text-anchor="middle">Send It</text>
      </g>

      <!-- show -->
      <line class="connector connector--dashed" x1="245" y1="254" x2="245" y2="300"/>
      <g class="step step--show">
        <rect class="icon-line" x="234" y="303" width="20" height="14" stroke-width="2"/>
        <rect class="icon" x="241" y="318" width="6" height="3"/>
        <rect class="icon-line" x="266" y="303" width="9" height="18" rx="2" stroke-width="1.6"/>
        <text class="step-label" x="245" y="337" text-anchor="middle">Show It</text>
      </g>
    </g>

    <!-- Benefits -->
    <line class="rule" x1="55" y1="381" x2="352" y2="381"/>
    <g class="benefits">
      <text class="benefit" x="203" y="392" text-anchor="middle">Don't keep your Treasured old photos under the bed anymore</text>
      <text class="benefit" x="203" y="406" text-anchor="middle">Breath new life into them</text>
      <text class="benefit" x="203" y="420" text-anchor="middle">Preserve them for life</text>
      <text class="benefit" x="203" y="434" text-anchor="middle">Digitize them and watch on your TV or Computer anytime</text>
      <text class="benefit" x="203" y="448" text-anchor="middle">Protect them from Fire, Flood or Damage</text>
    </g>
    <line class="rule" x1="55" y1="453" x2="352" y2="453"/>
    <text class="web" x="55" y="460">www.pictovault.com.au</text>

    <!-- Offer -->
    <text class="offer" x="203" y="505" text-anchor="middle">MAKE A GREAT CHRISTMAS GIFT</text>
    <text class="offer" x="203" y="525" text-anchor="middle">500 PHOTOS SCANNED FOR ONLY $50.00</text>
  </svg>

</main>
</body>
</html>
```